Reach For Summit needs a new design for Business Cards

We need a business card design for our personal training business call Reach For Summit. We are the Sustained Weight Loss Specialists.
Our target market is overweight and obese adults who have experience the ups of loosing weight and lows of putting it back on and are looking for a sustained weight loss solution.
Our USP is: "We Smash Through The Barriers That Are Holding You Back From Sustained Weight Loss".
We would like to the design incorporate the colours of our logo, with other acceptable colours being black, white, yellow and green.
Visit our website at www.reachforsummit.com.au for an overview of our business, and also the attached company profile.

Target Market(s)

Industry/Entity Type

Training

Colors
0092cd
eb1f27
fbed22
9bcb3c
000000
ffffff

Requirements
Must have
• Easy to read fonts
Logo (Not huge)
Call to Action (Something like, Claim your 10 Tips to Melt Body Fat, and 30 minutes PT Session VALUED AT $101)
Contact and Address details (as per footer of company profile (page 2 onwards)
List of Benefits (see company profile and website)
USP as per project overview
A picture to match the USP
Should not have
• Please do not try and copy the design of the company profile. It was slapped together.
A list of exercises

```html
<!DOCTYPE html>
<html lang="en">
<head>
<meta charset="utf-8">
<title>Reach For Summit – Business Card</title>
<link rel="stylesheet" href="https://fonts.googleapis.com/css2?family=Arimo:wght@400;700&display=swap">
<style>
  :root {
    --bg: #e9e6e2;
    --card: #000000;
    --blue: #0092cd;
    --red: #eb1f27;
    --yellow: #fbed22;
    --green: #9bcb3c;
    --white: #ffffff;
    --muted: #cfcfcf;
    --rule: #6b6b6b;
    --photo-top: #8d97a3;
    --photo-mid: #4f7fae;
    --photo-bottom: #c9c4bd;
  }
  * { margin: 0; padding: 0; box-sizing: border-box; }
  html, body { width: 1200px; height: 952px; overflow: hidden; }
  body { background: var(--bg); position: relative; font-family: "Arimo", Arial, sans-serif; }

  .card {
    position: absolute;
    background: var(--card);
    border-radius: 18px;
    overflow: hidden;
    box-shadow: 0 4px 14px rgba(0,0,0,.25);
  }
  .card--front { left: 39px; top: 26px; width: 741px; height: 423px; }
  .card--back  { left: 405px; top: 481px; width: 739px; height: 424px; }

  .brand-name {
    font-weight: 700;
    color: var(--red);
    white-space: nowrap;
  }
  .brand-mark {
    display: inline-block;
    width: 14px; height: 14px;
    border-radius: 50%;
    background: var(--red);
    vertical-align: middle;
    margin-right: 10px;
    position: relative; top: -3px;
  }
  .tagline { font-weight: 400; color: var(--red); }

  /* Front */
  .front-brand { position: absolute; left: 0; top: 0; width: 390px; text-align: center; }
  .front-brand .brand-name { position: absolute; top: 222px; left: 0; width: 100%; font-size: 32px; }
  .front-brand .tagline { position: absolute; top: 280px; left: 0; width: 100%; font-size: 16px; }

  .divider { position: absolute; left: 408px; top: 98px; width: 2px; height: 184px; background: var(--rule); }

  .contact { position: absolute; left: 421px; top: 94px; list-style: none; }
  .contact li { display: flex; align-items: center; height: 32px; color: var(--white); font-size: 18px; }
  .contact svg { width: 16px; height: 16px; margin-right: 9px; flex: none; }
  .address { position: absolute; left: 421px; top: 226px; color: var(--white); font-size: 18px; line-height: 28px; }

  .swoosh { position: absolute; left: 0; top: 0; }

  .person { position: absolute; left: 470px; top: 355px; width: 250px; text-align: center; color: var(--white); }
  .person__name { font-weight: 700; font-size: 23px; line-height: 28px; }
  .person__title { font-size: 17px; line-height: 22px; }

  /* Back */
  .back-info { position: absolute; left: 28px; top: 34px; width: 340px; text-align: center; }
  .back-info .brand-name { font-size: 28px; line-height: 34px; }
  .back-info .tagline { font-size: 16px; line-height: 22px; margin-top: 6px; }
  .usp {
    margin-top: 22px;
    color: var(--white);
    font-weight: 700;
    font-size: 15px;
    line-height: 20px;
  }
  .benefits { list-style: none; margin-top: 18px; text-align: left; padding-left: 30px; }
  .benefits li { display: flex; align-items: center; color: var(--muted); font-size: 14px; line-height: 24px; }
  .benefits svg { width: 14px; height: 14px; margin-right: 9px; flex: none; }
  .offer {
    margin-top: 20px;
    border-top: 2px solid var(--blue);
    padding-top: 12px;
    color: var(--white);
    font-size: 13px;
    line-height: 19px;
  }
  .offer strong { color: var(--yellow); font-weight: 700; }

  .photo {
    position: absolute; left: 396px; top: 0; width: 343px; height: 100%;
    background: linear-gradient(180deg, var(--photo-top) 0%, var(--photo-mid) 45%, var(--photo-bottom) 100%);
  }
</style>
</head>
<body>

  <section class="card card--front">
    <div class="front-brand">
      <div class="brand-name"><span class="brand-mark"></span>Reach For Summit</div>
      <div class="tagline">Sustained Weight Loss Specialists</div>
    </div>

    <div class="divider"></div>

    <ul class="contact">
      <li>
        <svg viewBox="0 0 16 16"><circle cx="8" cy="8" r="8" fill="var(--blue)"/><path d="M5.3 4.2l1.5 1.6-.8 1.2c.6 1.3 1.6 2.3 2.9 2.9l1.2-.8 1.6 1.5-1 1.3c-3 0-6.6-3.6-6.6-6.6z" fill="#fff"/></svg>
        0400 555 218
      </li>
      <li>
        <svg viewBox="0 0 16 16"><circle cx="8" cy="8" r="8" fill="var(--blue)"/><rect x="4" y="5.2" width="8" height="5.6" fill="#fff"/><path d="M4 5.2l4 3 4-3" fill="none" stroke="var(--blue)" stroke-width="1"/></svg>
        daniel@reachforsummit.com.au
      </li>
      <li>
        <svg viewBox="0 0 16 16"><circle cx="8" cy="8" r="8" fill="var(--blue)"/><circle cx="8" cy="8" r="4.6" fill="none" stroke="#fff" stroke-width="1"/><ellipse cx="8" cy="8" rx="2" ry="4.6" fill="none" stroke="#fff" stroke-width="1"/><line x1="3.4" y1="8" x2="12.6" y2="8" stroke="#fff" stroke-width="1"/></svg>
        www.reachforsummit.com.au
      </li>
    </ul>

    <p class="address">14 Banksia Rd<br>Riverton, Qld, 4108</p>

    <svg class="swoosh" width="741" height="423" viewBox="0 0 741 423">
      <path d="M0,356 C200,398 420,352 741,322 L741,423 L0,423 Z" fill="var(--red)"/>
      <path d="M0,392 C230,430 430,370 741,346 L741,423 L0,423 Z" fill="var(--card)"/>
      <path d="M0,335 C210,382 430,330 741,303 L741,310 C430,340 210,392 0,345 Z" fill="var(--blue)"/>
      <path d="M140,423 C330,410 480,355 741,340 L741,423 Z" fill="var(--blue)"/>
    </svg>

    <div class="person">
      <div class="person__name">Daniel Hartley</div>
      <div class="person__title">Manager</div>
    </div>
  </section>

  <section class="card card--back">
    <div class="back-info">
      <div class="brand-name"><span class="brand-mark"></span>Reach For Summit</div>
      <div class="tagline">Sustained Weight Loss Specialists</div>
      <p class="usp">We Smash Through The Barriers That Are Holding You Back From Sustained Weight Loss</p>
      <ul class="benefits">
        <li><svg viewBox="0 0 14 14"><circle cx="7" cy="7" r="7" fill="var(--green)"/><path d="M3.8 7.2l2.2 2.2 4.2-4.6" fill="none" stroke="#fff" stroke-width="1.6"/></svg>Lose the weight and keep it off</li>
        <li><svg viewBox="0 0 14 14"><circle cx="7" cy="7" r="7" fill="var(--green)"/><path d="M3.8 7.2l2.2 2.2 4.2-4.6" fill="none" stroke="#fff" stroke-width="1.6"/></svg>Personal plans built around you</li>
        <li><svg viewBox="0 0 14 14"><circle cx="7" cy="7" r="7" fill="var(--green)"/><path d="M3.8 7.2l2.2 2.2 4.2-4.6" fill="none" stroke="#fff" stroke-width="1.6"/></svg>Ongoing support and accountability</li>
      </ul>
      <p class="offer">Claim your <strong>10 Tips to Melt Body Fat</strong> and a<br><strong>30 minute PT Session – VALUED AT $101</strong></p>
    </div>
    <div class="photo" role="img" aria-label="Photograph of a father and young son running together in a road race, wearing blue shirts and race bibs, other runners behind them"></div>
  </section>

</body>
</html>
```